Everything fresh, everything new

When I take over the practice, I would like to breathe new life into the practice. I want a business card design that catches the eye and brings a breath of fresh air

```html
<!DOCTYPE html>
<html lang="en">
<head>
<meta charset="utf-8">
<title>Quellwerk – Business Card</title>
<link rel="stylesheet" href="https://fonts.googleapis.com/css2?family=Poppins:wght@400;500;600;700&display=swap">
<style>
  :root {
    --brand-green: #8cc63f;
    --charcoal: #4a4a4d;
    --ink: #3d3d40;
    --paper: #ffffff;
    --backdrop: #e6e7e8;
    --soft-line: #d9dadb;
  }
  * { margin: 0; padding: 0; box-sizing: border-box; }
  html, body { width: 1200px; height: 900px; overflow: hidden; }
  body {
    background: var(--backdrop);
    font-family: "Poppins", sans-serif;
    position: relative;
  }
  .card {
    position: absolute;
    left: 260px;
    width: 680px;
    height: 388px;
    border-radius: 22px;
    overflow: hidden;
    box-shadow: 0 6px 18px rgba(0,0,0,.18);
  }
  .card--back { top: 40px; }
  .card--front { top: 472px; }

  .pattern-fill {
    width: 100%; height: 100%;
    background: linear-gradient(135deg, #93cc45 0%, var(--brand-green) 55%, #7fb936 100%);
  }

  .front-shape { position: absolute; inset: 0; }

  .brand {
    position: absolute;
    left: 70px; top: 165px;
    display: flex; align-items: center; gap: 14px;
  }
  .brand__dot {
    width: 48px; height: 48px;
    border: 5px solid var(--brand-green);
    border-radius: 50%;
  }
  .brand__name {
    font-size: 40px; font-weight: 600;
    color: var(--ink); letter-spacing: -0.5px;
  }

  .contact {
    position: absolute;
    left: 455px; top: 62px;
    color: var(--paper);
  }
  .contact__name {
    font-size: 23px; font-weight: 700;
    color: var(--brand-green);
    text-transform: uppercase; letter-spacing: .2px;
    line-height: 1.1;
  }
  .contact__role { font-size: 15px; font-weight: 400; margin-top: 2px; }
  .contact__address {
    font-size: 14px; line-height: 1.45;
    margin-top: 30px; margin-left: 30px;
  }
  .contact__lines {
    list-style: none;
    font-size: 14px; line-height: 1.5;
    margin-top: 26px; margin-left: 48px;
  }
  .contact__lines li { display: flex; align-items: center; gap: 7px; }
  .contact__lines svg { width: 12px; height: 12px; fill: var(--paper); flex: none; }
</style>
</head>
<body>

  <section class="card card--back">
    <div class="pattern-fill" role="img" aria-label="Repeating embossed brand pattern on green"></div>
  </section>

  <section class="card card--front">
    <svg class="front-shape" viewBox="0 0 680 388" preserveAspectRatio="none" aria-hidden="true">
      <rect width="680" height="388" fill="var(--charcoal)"/>
      <circle cx="150" cy="210" r="296" fill="var(--soft-line)"/>
      <circle cx="150" cy="210" r="292" fill="var(--brand-green)"/>
      <circle cx="150" cy="210" r="281" fill="var(--paper)"/>
    </svg>

    <div class="brand">
      <span class="brand__dot"></span>
      <span class="brand__name">Quellwerk</span>
    </div>

    <div class="contact">
      <p class="contact__name">Jonas Keller</p>
      <p class="contact__role">Director</p>
      <p class="contact__address">1024 Budapest, Lomb utca<br>12. 2 floor 4.</p>
      <ul class="contact__lines">
        <li>
          <svg viewBox="0 0 24 24"><path d="M6.6 10.8a15 15 0 0 0 6.6 6.6l2.2-2.2a1 1 0 0 1 1-.25 11.4 11.4 0 0 0 3.6.57 1 1 0 0 1 1 1V20a1 1 0 0 1-1 1A17 17 0 0 1 3 4a1 1 0 0 1 1-1h3.5a1 1 0 0 1 1 1c0 1.25.2 2.45.57 3.6a1 1 0 0 1-.25 1z"/></svg>
          +36 30 555 0142
        </li>
        <li>
          <svg viewBox="0 0 24 24"><path d="M2 5h20v14H2z" opacity=".0"/><path d="M2 6l10 7 10-7v12H2z"/><path d="M2 5h20l-10 7z"/></svg>
          info@quellwerk.hu
        </li>
        <li>
          <svg viewBox="0 0 24 24"><path d="M12 2a10 10 0 1 0 0 20 10 10 0 0 0 0-20zm6.9 6h-3a15 15 0 0 0-1.3-3.9A8 8 0 0 1 18.9 8zM12 4a13 13 0 0 1 1.9 4h-3.8A13 13 0 0 1 12 4zM4.3 14a8 8 0 0 1 0-4h3.4a16 16 0 0 0 0 4zm.8 2h3a15 15 0 0 0 1.3 3.9A8 8 0 0 1 5.1 16zm3-8h-3a8 8 0 0 1 4.3-3.9A15 15 0 0 0 8.1 8zM12 20a13 13 0 0 1-1.9-4h3.8A13 13 0 0 1 12 20zm2.3-6H9.7a14 14 0 0 1 0-4h4.6a14 14 0 0 1 0 4zm.3 5.9a15 15 0 0 0 1.3-3.9h3a8 8 0 0 1-4.3 3.9zm1.7-5.9a16 16 0 0 0 0-4h3.4a8 8 0 0 1 0 4z"/></svg>
          www.quellwerk.hu
        </li>
      </ul>
    </div>
  </section>

</body>
</html>
```